Dentist Seminar invite please see .doc in attachments

Need an 8.5 x 11 invite designed. It will be for an invitation to attend an evening seminar on dental procedures. Feel free to utilize both front and back ONLY IF REQUIRED

See Assets & PPT with additional assets.

INSPIRATION: FIle NAME KOLVEN

Target Market(s)

Dentists

Industry/Entity Type

Dental

Other font styles liked:
• lato, garamond, palatino linotype

Colors
cee9f5
9bcb3c
0492cd
cadf82

Requirements
Must have
• Must have the colours suggested, and professional feel.
• Some of the assets merged cleanly into the design
Should not have
• Any pictures of teeth, tooth brushes or any dental product

```html
<!DOCTYPE html>
<html lang="en">
<head>
<meta charset="utf-8">
<title>Seminar Invitation – Global Excellence in Dentistry</title>
<link href="https://fonts.googleapis.com/css2?family=Lato:wght@400;700&family=EB+Garamond:wght@400&display=swap" rel="stylesheet">
<style>
  :root{
    --blue:#0492cd;
    --green:#9bcb3c;
    --sky:#cee9f5;
    --lime:#cadf82;
    --dark:#3b3b3d;
    --ink:#222222;
    --white:#ffffff;
    --stage:#5f5f5f;
  }
  *{box-sizing:border-box;margin:0;padding:0}
  html,body{width:1200px;height:1200px;overflow:hidden;background:var(--stage);font-family:"Lato",sans-serif}
  .canvas{position:relative;width:1200px;height:1200px}
  .page{position:absolute;top:270px;width:510px;height:660px;overflow:hidden}
  .page--front{left:60px;background:var(--white)}
  .page--back{left:630px;background:var(--dark)}
  .page__shapes{position:absolute;inset:0;width:510px;height:660px}
  .block{position:absolute}

  .brand{font-family:"Lato",sans-serif;font-weight:700;font-size:21px;letter-spacing:-0.3px;line-height:1}
  .brand--front{right:29px;top:228px;color:var(--ink)}
  .brand--back{left:27px;top:158px;color:var(--white)}

  .headline{right:29px;top:262px;text-align:right}
  .headline__lead{font-family:"EB Garamond",serif;color:var(--blue);font-size:22px;line-height:1.05}
  .headline__main{font-family:"Lato",sans-serif;font-size:15.5px;color:var(--ink);line-height:1.35;letter-spacing:0.2px}
  .rule{position:absolute;height:1.5px;background:var(--blue)}

  .label{font-family:"Lato",sans-serif;font-size:11px;letter-spacing:0.2px;line-height:1.3}
  .label--blue{color:var(--blue)}
  .label--white{color:var(--white)}

  .synopsis-title{right:32px;top:374px;text-align:right;font-weight:700}
  .synopsis{left:275px;top:395px;width:204px;font-size:7.2px;line-height:9.6px;color:var(--ink);text-align:justify;text-align-last:right}
  .web{right:32px;top:598px;font-family:"EB Garamond",serif;font-size:15px;color:var(--ink)}

  .objectives-title{left:34px;top:324px}
  .objectives{left:26px;top:370px;width:156px;list-style:none;font-size:7.2px;line-height:9.4px;color:var(--white)}
  .objectives li{position:relative;padding-left:9px;margin-bottom:3.4px;text-align:justify}
  .objectives li::before{content:"";position:absolute;left:0;top:2px;width:5px;height:5px;border-radius:50%;background:var(--blue);box-shadow:0 0 0 1px rgba(4,146,205,.35)}

  .event{right:55px;top:36px;text-align:right;color:var(--ink)}
  .event__date{font-size:24px;line-height:27px;font-weight:400;color:var(--white)}
  .event__date--second{color:var(--ink)}
  .event__venue{margin-top:10px;font-size:15.5px;line-height:19px;color:var(--white)}
  .event__address{font-size:15.5px;line-height:19px;color:var(--ink);font-weight:700}
  .event__reg{margin-top:10px;font-size:15.5px;line-height:19px;color:var(--white)}
  .event__contact{font-size:15.5px;line-height:19px;color:var(--ink);font-weight:700}

  .bio-title{left:27px;top:203px}
  .bio{left:27px;top:220px;width:232px;font-size:7.2px;line-height:9.6px;color:var(--white)}
</style>
</head>
<body>
<div class="canvas">

  <!-- Front page -->
  <section class="page page--front">
    <svg class="page__shapes" viewBox="0 0 510 660" aria-hidden="false">
      <defs>
        <linearGradient id="photoTone" x1="0" y1="0" x2="1" y2="1">
          <stop offset="0" stop-color="#f2ece4"/>
          <stop offset="0.5" stop-color="#b08466"/>
          <stop offset="1" stop-color="#4b3a33"/>
        </linearGradient>
        <linearGradient id="streak" x1="0" y1="1" x2="1" y2="0">
          <stop offset="0" stop-color="#0b5fb0"/>
          <stop offset="0.5" stop-color="#0492cd"/>
          <stop offset="1" stop-color="#7fd0f0"/>
        </linearGradient>
      </defs>
      <polygon points="0,180 335,180 200,640 0,640" fill="var(--dark)"/>
      <polygon points="360,0 510,0 510,163 283,220" fill="url(#streak)"/>
      <polygon points="0,188 0,260 60,250" fill="url(#streak)"/>
      <polyline points="0,186 205,340 428,66" fill="none" stroke="var(--green)" stroke-width="4" stroke-linejoin="round"/>
      <path role="img" aria-label="Photo of a smiling couple" d="M0,0 H410 Q440,0 440,30 Q440,50 428,66 L205,336 Q198,342 190,336 L0,186 Z" fill="url(#photoTone)"/>
      <rect x="0" y="640" width="510" height="20" fill="var(--green)"/>
      <rect x="404" y="334" width="76" height="1.5" fill="var(--blue)"/>
      <rect x="34" y="356" width="42" height="1.5" fill="var(--blue)"/>
    </svg>

    <div class="block brand brand--front">Veridana Group</div>

    <div class="block headline">
      <p class="headline__lead">United for</p>
      <p class="headline__main">GLOBAL EXCELLENCE</p>
      <p class="headline__main">IN DENTISTRY</p>
    </div>

    <div class="block label label--blue objectives-title">LEARNING<br><span class="label--white">OBJECTIVES:</span></div>
    <ul class="block objectives">
      <li>Discuss the use of modern digital technologies like CBCT, intra-oral scanning, and 3D printing.</li>
      <li>Learn to digitally plan surgical procedures and use 3D printed surgical guides</li>
      <li>Understand the benefits of microsurgery and the use of surgical operating microscope</li>
      <li>Understand the benefits of digital technology in surgical treatment planning</li>
      <li>Understanding and benefits of live guided navigation surgery and its applications</li>
      <li>Learn about innovative procedures like digitally guided bone block harvesting, digitally created bone grafts, and osteotomy guides.</li>
      <li>Understand how computer automated design software can improve upon real live surgery.</li>
    </ul>

    <div class="block label label--blue synopsis-title">SYNOPSIS:</div>
    <p class="block synopsis">This presentation will cover the recent advances in digital technology and its use in dentistry. Digital protocols will be introduced that can improve upon traditional treatment planning approaches. The use of modern 3D technology and the digital workflow can simplify advanced procedures enhancing the predictability of the surgical outcomes. Through the use of state of the art diagnostic imaging technologies, intra-oral scanning, live guided navigation, and 3D printing; multiple digital workflows and their surgical applications will be discussed through real clinical cases from Dr Almeric's surgical practice. This groundbreaking lecture will showcase the synergy between advanced technology and fundamental biological principles to revolutionize the modern practice of periodontics and implantology. Multiple innovative protocols to treat advanced surgical cases will be presented with techniques that have never been seen before.</p>

    <div class="block web">www.veridanagroup.com</div>
  </section>

  <!-- Back page -->
  <section class="page page--back">
    <svg class="page__shapes" viewBox="0 0 510 660">
      <polygon points="142,73 192,12 510,12 510,219 424,296" fill="var(--blue)" stroke="var(--blue)" stroke-width="28" stroke-linejoin="round"/>
      <polygon points="0,405 38,369 295,593 253,660 0,660" fill="var(--white)"/>
      <polygon points="392,628 460,545 510,582 510,660 430,660" fill="var(--green)"/>
      <polygon points="347,660 403,590 467,660" fill="var(--white)"/>
      <rect x="72" y="348" width="133" height="104" rx="12" fill="var(--blue)" role="img" aria-label="3D scan of a lower jaw with planned implants"/>
      <rect x="225" y="348" width="133" height="104" rx="12" fill="var(--blue)" role="img" aria-label="3D surgical guide model over an upper arch"/>
      <rect x="72" y="466" width="133" height="104" rx="12" fill="var(--blue)" role="img" aria-label="3D scan of an upper jaw"/>
      <rect x="225" y="466" width="133" height="104" rx="12" fill="var(--blue)" role="img" aria-label="3D scan of a lower jaw with implant placement"/>
      <rect x="27" y="183" width="76" height="1.5" fill="var(--blue)"/>
    </svg>

    <div class="block event">
      <p class="event__date">NOVEMBER 13</p>
      <p class="event__date event__date--second">2017/ 6:30 – 9:30PM</p>
      <p class="event__venue">MAPLE CREST BANQUET HALL</p>
      <p class="event__address">880 Harwick Ave. Toronto,<br>Ontario M1W 3K7</p>
      <p class="event__reg">REGISTRATION:</p>
      <p class="event__contact">r.lunde@email.com<br>416-555-0142</p>
    </div>

    <div class="block brand brand--back">Veridana Group</div>

    <div class="block label label--blue bio-title">BIOGRAPHY</div>
    <p class="block bio">Lorem Ipsum is simply dummy text of the printing and typesetting industry. Lorem Ipsum has been the industry's standard dummy text ever since the 1500s, when an unknown printer took a galley of type and scrambled it to make a type specimen book. It has survived not only five centuries, but also the leap into electronic typesetting, remaining essentially unchanged. It was popularised in the 1960s with the release of Letraset sheets containing Lorem Ipsum passages, and more recently with desktop publishing software like Aldus PageMaker including versions of</p>
  </section>

</div>
</body>
</html>
```